Somaliland Vs Sealand

We are hosting an international football match between Somaliland and Sealand, to celebrate the 23rd independence anniversary of Somaliland. I need a flyer to promote the game. The Match will be taking place on Saturday the 17/05/2014, kick off is at 2pm. The Venue will be, Marwick Park Stadium, Tottenham, London, N19 4QB.
Enclosed, I have attached files of each countries national football emblem and their national flags colours.
I have enclosed few flyers for your attention of possible designs to take lead from.

I would like each countries flags to appear in circle shapes if possible and somehow include small images of the national flags, perhaps on the edges of the flyer.
£5 entry for tickets, all donations for charity.

Charity

```html
<!DOCTYPE html>
<html lang="en">
<head>
<meta charset="utf-8">
<title>Somaliland vs Sealand – Match Flyer</title>
<link rel="stylesheet" href="https://fonts.googleapis.com/css2?family=Oswald:wght@300;400;700&display=swap">
<style>
  :root {
    --page-bg: #d9d9d9;
    --flyer-black: #000000;
    --silver-top: #ffffff;
    --silver-bottom: #8d9299;
    --vs-blue: #3f7fb8;
    --date-yellow: #e6e81f;
    --kickoff-green: #6fb63a;
    --entry-green: #8fc45a;
    --badge-white: #ffffff;
    --flag-green: #2f8a4c;
    --flag-red: #c9352f;
    --stand-navy: #0b1a33;
    --pitch-green: #4d9a1f;
    --pitch-glow: #d8e43a;
  }
  html, body {
    margin: 0;
    width: 861px;
    height: 1200px;
    overflow: hidden;
    background: var(--page-bg);
  }
  .flyer {
    position: absolute;
    left: 79px;
    top: 88px;
    width: 703px;
    height: 995px;
    background: var(--flyer-black);
    overflow: hidden;
    font-family: "Oswald", "Arial Narrow", sans-serif;
    text-align: center;
  }
  .stadium-scene {
    position: absolute;
    inset: 0 0 auto 0;
    height: 745px;
    background:
      radial-gradient(ellipse 180px 90px at 50% 250px, #f4f4f4 0%, #bcbcbc 55%, transparent 100%),
      radial-gradient(ellipse 320px 180px at 50% 600px, var(--pitch-glow) 0%, var(--pitch-green) 55%, transparent 100%),
      linear-gradient(180deg,
        var(--flag-green) 0px,
        #e6e6e6 90px,
        #f1f1f1 140px,
        var(--flag-red) 200px,
        #3a1a22 250px,
        var(--stand-navy) 280px,
        #10284a 430px,
        var(--pitch-green) 500px,
        #3d7a18 610px,
        #0a0a0a 690px,
        var(--flyer-black) 745px);
  }
  .team-badge {
    position: absolute;
    width: 150px;
    color: var(--badge-white);
    font-weight: 400;
    font-size: 9px;
    line-height: 1.2;
  }
  .team-badge .badge-disc {
    display: block;
    margin: 0 auto 6px;
    width: 62px;
    height: 62px;
    border-radius: 50%;
    background: var(--badge-white);
  }
  .team-badge--home { left: -4px; top: 292px; }
  .team-badge--away { left: 535px; top: 385px; }
  .team-name {
    position: absolute;
    left: 0;
    right: 0;
    margin: 0;
    font-weight: 700;
    font-size: 76px;
    line-height: 1;
    letter-spacing: 1px;
    color: var(--silver-top);
    background: linear-gradient(180deg, var(--silver-top) 30%, var(--silver-bottom) 100%);
    -webkit-background-clip: text;
    background-clip: text;
    -webkit-text-fill-color: transparent;
  }
  .team-name--home { top: 300px; }
  .team-name--away { top: 395px; }
  .team-name .vs {
    background: linear-gradient(180deg, #7fb2e0 20%, var(--vs-blue) 100%);
    -webkit-background-clip: text;
    background-clip: text;
    margin-right: 18px;
  }
  .match-date {
    position: absolute;
    top: 770px;
    left: 0; right: 0;
    margin: 0;
    color: var(--date-yellow);
    font-weight: 400;
    font-size: 38px;
    letter-spacing: 6px;
    word-spacing: 14px;
  }
  .kick-off {
    position: absolute;
    top: 818px;
    left: 0; right: 0;
    margin: 0;
    color: var(--kickoff-green);
    font-weight: 700;
    font-size: 56px;
    letter-spacing: 2px;
    line-height: 1.1;
  }
  .venue {
    position: absolute;
    top: 880px;
    left: 0; right: 0;
    margin: 0;
    color: var(--kickoff-green);
    font-weight: 700;
    font-size: 19px;
    letter-spacing: 0.5px;
  }
  .entry {
    position: absolute;
    top: 944px;
    left: 0; right: 0;
    margin: 0;
    color: var(--entry-green);
    font-weight: 300;
    font-size: 22px;
    letter-spacing: 1px;
  }
</style>
</head>
<body>
  <main class="flyer">
    <div class="stadium-scene" role="img" aria-label="Somaliland and Sealand flags waving over a floodlit stadium with a football in the centre, a green pitch and silhouettes of cheering fans waving flags"></div>

    <div class="team-badge team-badge--home">
      <span class="badge-disc"></span>
      Horn Football Union
    </div>

    <h1 class="team-name team-name--home">SOMALILAND</h1>
    <h1 class="team-name team-name--away"><span class="vs">VS</span>SEALAND</h1>

    <div class="team-badge team-badge--away">
      <span class="badge-disc"></span>
      Fortress Football Union
    </div>

    <p class="match-date">SATURDAY 17/05/2014</p>
    <p class="kick-off">KICK OFF AT 2PM</p>
    <p class="venue">MARWICK PARK STADIUM, TOTTENHAM, LONDON, N19 4QB</p>
    <p class="entry">Entry: £5</p>
  </main>
</body>
</html>
```